Book Cover for a novel

I need a book cover. I have attached the book cover for the first book in this series. It is a clean contemporary Christian romance.
I like this image from PixVault and would love it if the designer can use this image.
https://www.pixvaultimages.example/photo/a-quiet-morning-in-the-garden-kt482917305-903746118
Book Title: Come Home Slowly (I want the fonts to remain the same as the last book for brand consistency)
Author: LENA MARSH (please put this in all caps at the bottom of the cover)
Blurb: Find it attached in the Word Doc.
I would like an Brightshelf eBook cover as well as the full cover for an 5 x 8 BOOK which is 185 pages long.

```html
<!DOCTYPE html>
<html lang="en">
<head>
<meta charset="utf-8">
<title>Come Home Slowly – Full Cover</title>
<link rel="stylesheet" href="https://fonts.googleapis.com/css2?family=Poppins:wght@300;400;600;700&family=Mrs+Saint+Delafield&display=swap">
<style>
  :root {
    --backdrop: #bcc8cb;
    --cover-dark: #2a1b15;
    --cover-mid: #4a362d;
    --cover-light: #6b5549;
    --ink: #ffffff;
    --ink-soft: #efe6e1;
    --rule: rgba(255,255,255,0.45);
    --photo-warm: #c98a4e;
    --photo-glow: #e9c08a;
    --photo-shade: #3a241a;
    --photo-blue: #6f7f9c;
  }
  * { margin: 0; padding: 0; box-sizing: border-box; }
  html, body { width: 1200px; height: 800px; overflow: hidden; background: var(--backdrop); }
  .wrap {
    position: absolute; left: 150px; top: 60px;
    width: 900px; height: 680px;
    display: flex;
    box-shadow: 0 14px 40px rgba(0,0,0,0.25);
  }
  /* Back cover */
  .back {
    width: 425px; height: 100%;
    background: linear-gradient(170deg, var(--cover-light) 0%, var(--cover-mid) 35%, var(--cover-dark) 100%);
    color: var(--ink);
    font-family: 'Poppins', sans-serif;
    text-align: center;
    padding: 58px 30px 0;
  }
  .back-hook { font-weight: 700; font-size: 15px; line-height: 1.35; margin-bottom: 30px; }
  .back-blurb p { font-weight: 300; font-size: 11.2px; line-height: 1.5; margin-bottom: 14px; color: var(--ink-soft); }
  .back-rule { border: none; border-top: 1px solid var(--rule); margin: 28px 0; }
  .back-series { font-weight: 400; font-size: 11.2px; line-height: 1.5; padding: 0 8px; }
  .about-title { font-weight: 700; font-size: 11.5px; margin-bottom: 2px; }
  .about-text { font-weight: 400; font-size: 11.2px; line-height: 1.45; padding: 0 6px; }
  /* Spine */
  .spine {
    width: 50px; height: 100%;
    background: linear-gradient(90deg, var(--cover-dark), #3a2920 50%, var(--cover-dark));
    color: var(--ink);
    display: flex; flex-direction: column; align-items: center; justify-content: space-between;
    padding: 26px 0 24px;
  }
  .spine-text { writing-mode: vertical-rl; white-space: nowrap; }
  .spine-author { font-family: 'Poppins', sans-serif; font-weight: 700; font-size: 14px; letter-spacing: 1px; }
  .spine-title { font-family: 'Poppins', sans-serif; font-weight: 600; font-size: 18px; }
  .spine-title .script { font-family: 'Mrs Saint Delafield', cursive; font-weight: 400; font-size: 40px; margin-top: 8px; }
  /* Front cover */
  .front { position: relative; width: 425px; height: 100%; overflow: hidden; }
  .front-photo {
    position: absolute; inset: 0;
    background:
      radial-gradient(ellipse at 70% 35%, var(--photo-glow) 0%, transparent 45%),
      radial-gradient(ellipse at 62% 72%, var(--photo-blue) 0%, transparent 40%),
      linear-gradient(180deg, var(--photo-shade) 0%, var(--photo-warm) 40%, #a8744a 70%, var(--photo-shade) 100%);
  }
  .front-title {
    position: absolute; top: 28px; left: 0; right: 0;
    display: flex; align-items: flex-start; justify-content: center;
    color: var(--ink);
  }
  .front-title .plain { font-family: 'Poppins', sans-serif; font-weight: 600; font-size: 28px; margin-top: 40px; }
  .front-title .script { font-family: 'Mrs Saint Delafield', cursive; font-size: 92px; line-height: 1; margin-left: 8px; }
  .front-author {
    position: absolute; bottom: 34px; left: 0; right: 0;
    text-align: center; color: var(--ink);
    font-family: 'Poppins', sans-serif; font-weight: 700; font-size: 30px; letter-spacing: 1px;
  }
</style>
</head>
<body>
<main class="wrap">
  <section class="back">
    <h2 class="back-hook">She’s falling hard for the guy next door.<br>The only problem? He’s her landlord.</h2>
    <div class="back-blurb">
      <p>When outspoken Dr. Nadia Hollis returns home from volunteering in South America, she’s a broken woman who needs a fresh start. So when a childhood friend recommends the extra apartment in his best friend’s duplex, Nadia is more than grateful. What she doesn’t expect is for her landlord to be an attractive ER doctor.</p>
      <p>Dr. Evan Pryor is a volunteer youth minister whose past has kept him from forming close relationships with anyone. But he can’t resist his tenant Nadia’s kindness and friendliness. As sparks begin to fly between them, Evan discovers the secret Nadia has been hiding from everyone and he wonders if falling in love is worth it.</p>
      <p>Can the two overcome their pasts and allow themselves a chance at enduring love?</p>
    </div>
    <hr class="back-rule">
    <p class="back-series">Come Home Slowly is Book Two in The Harbor Street Doctors sweet contemporary Christian romance series. If you enjoy sweet romantic stories that also feature the power of God to heal broken hearts and lives, then you will love Come Home Slowly.</p>
    <hr class="back-rule">
    <h3 class="about-title">About The Author</h3>
    <p class="about-text">Lena Marsh is a writer saved by the Grace of God. She writes sweet romance books that feature the power of God to heal and restore any situation. Lena Marsh is married to a pastor and is absolutely enthralled by mountains and the ocean. She currently lives with her family in Southern California.</p>
  </section>

  <section class="spine">
    <span class="spine-text spine-author">Lena Marsh</span>
    <span class="spine-text spine-title">Come Home <span class="script">Slowly</span></span>
  </section>

  <section class="front">
    <div class="front-photo" role="img" aria-label="Cover photograph: a smiling couple embracing in a warmly lit home kitchen"></div>
    <h1 class="front-title"><span class="plain">Come Home</span><span class="script">Slowly</span></h1>
    <p class="front-author">LENA MARSH</p>
  </section>
</main>
</body>
</html>
```